Report Design Template Needed for Strategy Consulting Co.

I have a small consulting business that does market research, develops marketing strategy, and does business development work (sales, finding partners, preparing for investors) for small and medium-sized companies who can’t afford their own full-time marketing person.

Most of my reports are PowerPoint Decks. There is usually a Title Page, a Table of Contents, an Executive Summary, a Detailed Findings section (with some section breaks, so I need a divider page between sections), and a Recommendations section.

I need a report template/style that is attractive, professional and not too bold such that it takes away from the content, which is what they are paying for.

I have color palette ideas and graphics in the attached brief. Please let me know if you need anything else, or if you need graphic files.

Thank you!!

Target Market(s)

Small business professionals, scientists, business development executives.

Industry/Entity Type

Marketing

Font styles to use
Sans Serif

Requirements
Must have
• Should have the sections listed in the brief. Also, need to be able to import the template complete.
Should not have
• Background must not overtake the text

```html
<!DOCTYPE html>
<html lang="en">
<head>
<meta charset="utf-8">
<title>Horizon Partners – Presentation Template</title>
<link href="https://fonts.googleapis.com/css2?family=Oswald:wght@300;500;600&family=Open+Sans:ital,wght@0,400;0,600;1,700&display=swap" rel="stylesheet">
<style>
  :root {
    --canvas: #b3b3b3;
    --white: #ffffff;
    --gold: #f5a300;
    --sky: #5fa8d3;
    --teal: #1f6e73;
    --navy: #1b4674;
    --deep-navy: #17294a;
    --band-blue: #22527f;
    --title-blue: #3a8ab3;
    --olive: #7b8a1b;
    --rule: #9a9a9a;
    --body: #555a60;
    --faint: #eef0e2;
  }
  * { margin: 0; padding: 0; box-sizing: border-box; }
  html, body { width: 1200px; height: 900px; overflow: hidden; background: var(--canvas); }
  body { position: relative; font-family: "Open Sans", Arial, sans-serif; }

  .slide { position: absolute; width: 494px; height: 382px; background: var(--white); overflow: hidden; }
  .slide--title-teal { left: 112px; top: 70px; }
  .slide--summary-a { left: 622px; top: 70px; }
  .slide--title-navy { left: 112px; top: 470px; }
  .slide--summary-b { left: 622px; top: 470px; }

  .slide svg.shapes { position: absolute; left: 0; top: 0; width: 494px; height: 382px; }

  /* title slide */
  .title-bg { position: absolute; left: 0; top: 0; width: 494px; height: 270px; }
  .slide--title-teal .title-bg { background: linear-gradient(90deg, var(--sky) 0%, #3a8db0 45%, var(--teal) 100%); }
  .slide--title-navy .title-bg { background: linear-gradient(90deg, var(--sky) 0%, #2f6f9f 45%, var(--navy) 100%); }
  .team-photo { position: absolute; left: 0; top: 0; width: 340px; height: 262px;
    background: linear-gradient(90deg, rgba(150,200,230,.55) 0%, rgba(120,180,220,.35) 60%, rgba(120,180,220,0) 100%); }
  .welcome { position: absolute; right: 52px; top: 110px; text-align: right;
    font-family: "Oswald", "Arial Narrow", sans-serif; font-weight: 600; color: var(--gold);
    font-size: 25px; line-height: 32px; text-transform: uppercase; }
  .event-date { display: block; font-weight: 300; font-size: 14px; line-height: 20px; color: var(--white); text-transform: none; }
  .brand-name { position: absolute; right: 22px; top: 300px; font-family: "Open Sans", Arial, sans-serif;
    font-weight: 600; font-size: 25px; color: var(--deep-navy); letter-spacing: -0.5px; }
  .bottom-bar { position: absolute; left: 0; bottom: 0; width: 494px; height: 9px; background: var(--deep-navy); }

  /* summary slides */
  .section-title { position: absolute; left: 25px; top: 27px; font-family: "Oswald", "Arial Narrow", sans-serif;
    font-weight: 500; font-size: 18px; letter-spacing: .2px; color: var(--title-blue); }
  .section-title .accent { color: var(--olive); margin-left: 4px; }
  .title-rule { position: absolute; left: 25px; top: 51px; width: 444px; height: 1px; background: var(--rule); }

  .desk-photo { position: absolute; left: 25px; top: 58px; width: 444px; height: 103px;
    background: linear-gradient(110deg, #8e949a 0%, #dfe3e6 35%, #f4f5f6 70%, #d6dadd 100%); }
  .soft-motif { position: absolute; background: radial-gradient(ellipse at center, rgba(232,236,214,.8) 0%, rgba(232,236,214,.35) 55%, rgba(255,255,255,0) 80%); }
  .soft-motif--a { left: 20px; top: 220px; width: 130px; height: 130px; }
  .soft-motif--b { left: 20px; top: 225px; width: 180px; height: 120px; }
  .lead-caps { position: absolute; left: 25px; top: 184px; width: 150px; font-size: 8px; line-height: 12.4px;
    color: var(--title-blue); text-transform: uppercase; }
  .body-copy { position: absolute; left: 201px; top: 184px; width: 250px; font-size: 6.6px; line-height: 11.2px; color: var(--body); }
  .body-copy p + p { margin-top: 11px; }

  .footer-brand { position: absolute; left: 9px; top: 368px; font-size: 8px; font-weight: 600; color: var(--white); letter-spacing: -0.2px; }
  .footer-note { position: absolute; right: 12px; top: 371px; font-size: 5.6px; color: var(--white); }

  .highlight-band { position: absolute; left: 0; top: 95px; width: 494px; height: 100px; background: var(--band-blue); }
  .scout-photo { position: absolute; left: 24px; top: 82px; width: 177px; height: 137px;
    background: linear-gradient(135deg, #d7eef7 0%, #c9a98c 45%, #2c4756 75%, #b7d4e6 100%); }
  .band-quote { position: absolute; left: 216px; top: 114px; width: 244px; font-size: 8.6px; line-height: 17.6px;
    font-weight: 700; font-style: italic; color: var(--white); text-align: justify; }
  .band-body { position: absolute; left: 216px; top: 205px; width: 244px; font-size: 7.7px; line-height: 17.4px;
    color: var(--body); text-align: justify; }
</style>
</head>
<body>

<section class="slide slide--title-teal">
  <div class="title-bg"></div>
  <div class="team-photo" role="img" aria-label="Photo of a team seated at a meeting table"></div>
  <svg class="shapes" viewBox="0 0 494 382" aria-hidden="true">
    <defs>
      <linearGradient id="swoosh1" x1="0" x2="1" y1="0" y2="0">
        <stop offset="0" stop-color="#1f5f93"/><stop offset=".55" stop-color="#2d74a2"/>
        <stop offset=".8" stop-color="#b5bd6a"/><stop offset="1" stop-color="#6f7f12"/>
      </linearGradient>
    </defs>
    <path d="M0,258 C140,232 330,222 494,212 L494,240 C330,236 150,242 0,272 Z" fill="url(#swoosh1)"/>
    <path d="M0,272 C150,244 330,236 494,240 L494,382 L0,382 Z" fill="#ffffff"/>
    <path d="M60,250 C200,232 360,232 400,258" fill="none" stroke="#ffffff" stroke-width="1.2"/>
  </svg>
  <h1 class="welcome">Welcome<br>to our presentation<span class="event-date">Birmingham, August 25, 2013</span></h1>
  <div class="brand-name">Horizon Partners</div>
  <div class="bottom-bar"></div>
</section>

<section class="slide slide--summary-a">
  <h2 class="section-title">EXECUTIVE<span class="accent">SUMMARY</span></h2>
  <div class="title-rule"></div>
  <div class="desk-photo" role="img" aria-label="Photo of hands working at a laptop with printed charts"></div>
  <div class="soft-motif soft-motif--a" role="img" aria-label="Faint decorative light bulb motif"></div>
  <p class="lead-caps">Lorem ipsum dolor sit met consectur adipsicing elit, sed do euismod tempor incididunt ut labore et delore magna</p>
  <div class="body-copy">
    <p>Lorem ipsum dolor sit amet, consectetur adipisicing elit, sed do eiusmod tempor incididunt ut labore et dolore magna aliqua. Ut enim ad minim veniam, quis nostrud exercitation ullamco laboris nisi ut aliquip ex ea commodo consequat. Duis aute irure dolor in reprehenderit in voluptate velit esse cillum dolore eu fugiat nulla pariatur.</p>
    <p>Lorem ipsum dolor sit amet, consectetur adipisicing elit, sed do eiusmod tempor incididunt ut labore et dolore magna aliqua. Ut enim ad minim veniam, quis nostrud exercitation ullamco laboris nisi ut aliquip ex ea commodo consequat. Duis aute irure dolor in reprehenderit in voluptate velit esse cillum dolore eu fugiat nulla pariatur. Excepteur sint occaecat cupidatat non proident, sunt in culpa qui officia deserunt mollit anim id est laborum.</p>
  </div>
  <svg class="shapes" viewBox="0 0 494 382" aria-hidden="true">
    <defs>
      <linearGradient id="foot1" x1="0" x2="1"><stop offset="0" stop-color="#2a7d97"/><stop offset="1" stop-color="#1d3f68"/></linearGradient>
      <linearGradient id="green1" x1="0" x2="1"><stop offset="0" stop-color="#7b8a1b"/><stop offset=".6" stop-color="#c4c98a"/><stop offset="1" stop-color="#ffffff" stop-opacity="0"/></linearGradient>
    </defs>
    <path d="M0,330 C120,334 230,344 360,352 L0,358 Z" fill="url(#green1)"/>
    <path d="M0,358 C180,352 380,345 494,322 L494,382 L0,382 Z" fill="url(#foot1)"/>
    <path d="M100,340 C240,352 400,350 494,332" fill="none" stroke="#1d4f7f" stroke-width="1.5"/>
  </svg>
  <div class="footer-brand">Horizon Partners</div>
  <div class="footer-note">Proprietary and Confidential &nbsp;|&nbsp; 2</div>
</section>

<section class="slide slide--title-navy">
  <div class="title-bg"></div>
  <div class="team-photo" role="img" aria-label="Photo of a team seated at a meeting table"></div>
  <svg class="shapes" viewBox="0 0 494 382" aria-hidden="true">
    <defs>
      <linearGradient id="swoosh2" x1="0" x2="1" y1="0" y2="0">
        <stop offset="0" stop-color="#1f5f93"/><stop offset=".55" stop-color="#2d74a2"/>
        <stop offset=".8" stop-color="#b5bd6a"/><stop offset="1" stop-color="#6f7f12"/>
      </linearGradient>
    </defs>
    <path d="M0,258 C140,232 330,222 494,212 L494,240 C330,236 150,242 0,272 Z" fill="url(#swoosh2)"/>
    <path d="M0,272 C150,244 330,236 494,240 L494,382 L0,382 Z" fill="#ffffff"/>
    <path d="M60,250 C200,232 360,232 400,258" fill="none" stroke="#ffffff" stroke-width="1.2"/>
  </svg>
  <h1 class="welcome">Welcome<br>to our presentation<span class="event-date">Birmingham, August 25, 2013</span></h1>
  <div class="brand-name">Horizon Partners</div>
  <div class="bottom-bar"></div>
</section>

<section class="slide slide--summary-b">
  <h2 class="section-title">EXECUTIVE<span class="accent">SUMMARY</span></h2>
  <div class="title-rule"></div>
  <div class="highlight-band"></div>
  <div class="scout-photo" role="img" aria-label="Photo of a woman looking through binoculars"></div>
  <p class="band-quote">Lorem ipsum dolor sit amet, consectetur adipisicing elit, sed do eiusmod tempor incididunt ut labore et dolore magna aliqua. Ut enim ad minim veniam, quis nostrud exercitation ullamco laboris nisi ut aliquip ex ea commodo</p>
  <p class="band-body">Lorem ipsum dolor sit amet, consectetur adipisicing elit, sed do eiusmod tempor incididunt ut labore et dolore magna aliqua. Ut enim ad minim veniam, quis nostrud exercitation ullamco laboris nisi ut aliquip ex ea commodo consequat. Duis aute irure dolor in reprehenderit in voluptate velit esse cillum dolore eu fugiat nulla pariatur.</p>
  <div class="soft-motif soft-motif--b" role="img" aria-label="Faint decorative growth motif"></div>
  <svg class="shapes" viewBox="0 0 494 382" aria-hidden="true">
    <defs>
      <linearGradient id="foot2" x1="0" x2="1"><stop offset="0" stop-color="#2a7d97"/><stop offset="1" stop-color="#1d3f68"/></linearGradient>
      <linearGradient id="green2" x1="0" x2="1"><stop offset="0" stop-color="#7b8a1b"/><stop offset=".6" stop-color="#c4c98a"/><stop offset="1" stop-color="#ffffff" stop-opacity="0"/></linearGradient>
    </defs>
    <path d="M0,330 C120,334 230,344 360,352 L0,358 Z" fill="url(#green2)"/>
    <path d="M0,358 C180,352 380,345 494,322 L494,382 L0,382 Z" fill="url(#foot2)"/>
    <path d="M100,340 C240,352 400,350 494,332" fill="none" stroke="#1d4f7f" stroke-width="1.5"/>
  </svg>
  <div class="footer-brand">Horizon Partners</div>
  <div class="footer-note">Proprietary and Confidential &nbsp;|&nbsp; 2</div>
</section>

</body>
</html>
```